Veterinarian specialized in Equine (horse) sports medicine needs logo and stationary design!

New veterinary clinic only focused on horses needs logo and stationary designs. The clinic works with sport horses including jumping horses, dressage horses and polo horses (all disciplines you can find online. No racing horses). Name of clinic is StrideCare and is based in Mexico City where there is a large and elite clientele of sports horses. My main focus is orthopedics and rehabilitation.
I think logo should include horse(s), especially if they are performing a sport (like jumping, etc).

Target Market(s)

Elite horse-owners of sport horses.

Industry/Entity Type

Horseback Riding

Requirements
Must have
• Great Logo! I like bold and bright colors (no pastels), but with a professional tone.

```html
<!DOCTYPE html>
<html lang="en">
<head>
<meta charset="utf-8">
<title>StrideCare Stationery</title>
<link href="https://fonts.googleapis.com/css2?family=Montserrat:wght@400;500;700&display=swap" rel="stylesheet">
<style>
  :root {
    --orange: #e8682e;
    --charcoal: #3a3c40;
    --paper: #f4f4f3;
    --backdrop: #ebe5db;
    --white: #ffffff;
    --shadow: rgba(60, 45, 30, 0.25);
  }
  * { margin: 0; padding: 0; box-sizing: border-box; }
  html, body {
    width: 1117px; height: 1200px; overflow: hidden;
    background: var(--backdrop);
    font-family: "Montserrat", sans-serif;
  }
  .canvas { position: relative; width: 1117px; height: 1200px; }

  .letterhead {
    position: absolute; left: 210px; top: 60px; width: 630px; height: 809px;
    background: var(--paper);
    box-shadow: 0 6px 14px var(--shadow);
    overflow: hidden;
  }
  .corner-accent { position: absolute; top: 0; right: 0; }
  .brand-name {
    display: flex; align-items: center; gap: 10px;
    font-weight: 700; color: var(--charcoal); letter-spacing: -0.5px;
    white-space: nowrap;
  }
  .brand-dot { border-radius: 50%; background: var(--orange); flex: none; }
  .letterhead .brand-name { position: absolute; left: 32px; top: 128px; font-size: 44px; }
  .letterhead .brand-dot { width: 22px; height: 22px; }

  .contact-band {
    position: absolute; left: 0; bottom: 0; width: 100%; height: 61px;
    background: var(--orange); color: var(--white);
    display: flex; align-items: center; justify-content: center;
    gap: 16px; padding: 0 16px; font-size: 14px; font-weight: 400;
    white-space: nowrap;
  }
  .contact-item { display: flex; align-items: center; gap: 8px; }
  .contact-item svg { flex: none; }

  .card {
    position: absolute; top: 941px; width: 270px; height: 161px;
    background: var(--paper);
    box-shadow: 0 5px 10px var(--shadow);
    overflow: hidden;
  }
  .card-front { left: 225px; }
  .card-back { left: 551px; }
  .card svg.accent { position: absolute; top: 0; left: 0; }

  .card-front .brand-name {
    position: absolute; left: 0; right: 0; top: 60px; justify-content: center;
    font-size: 27px; gap: 7px;
  }
  .card-front .brand-dot { width: 13px; height: 13px; }

  .card-back .brand-name { position: absolute; left: 12px; top: 28px; font-size: 19px; gap: 5px; }
  .card-back .brand-dot { width: 9px; height: 9px; }
  .holder { position: absolute; left: 10px; top: 108px; }
  .holder-name { color: var(--orange); font-weight: 700; font-size: 12px; }
  .holder-role { color: var(--charcoal); font-size: 8px; }
  .card-contacts { position: absolute; right: 46px; top: 112px; list-style: none; }
  .card-contacts li {
    display: flex; align-items: center; justify-content: flex-end; gap: 4px;
    font-size: 7px; color: var(--charcoal); height: 16px; white-space: nowrap;
  }
  .card-contacts .tag {
    width: 22px; height: 8px; background: var(--charcoal);
    display: flex; align-items: center; justify-content: flex-start; padding-left: 2px;
  }
  .card-contacts .tag i { width: 4px; height: 4px; border-radius: 50%; background: var(--white); }
</style>
</head>
<body>
<main class="canvas">

  <section class="letterhead">
    <svg class="corner-accent" width="160" height="260" viewBox="470 0 160 260">
      <polygon points="487,0 630,0 630,248" fill="var(--orange)"/>
      <polygon points="545,118 557,112 630,234 630,256 622,254" fill="var(--charcoal)"/>
    </svg>
    <div class="brand-name"><span class="brand-dot"></span>StrideCare</div>

    <footer class="contact-band">
      <span class="contact-item">
        <svg width="14" height="16" viewBox="0 0 16 18"><rect x="3" y="1" width="10" height="16" rx="2" fill="none" stroke="#fff" stroke-width="2"/><circle cx="8" cy="13" r="1.4" fill="#fff"/></svg>
        000.111.1234
      </span>
      <span class="contact-item">
        <svg width="14" height="14" viewBox="0 0 16 16"><circle cx="8" cy="8" r="6.5" fill="none" stroke="#fff" stroke-width="1.8"/><circle cx="8" cy="8" r="2.5" fill="none" stroke="#fff" stroke-width="1.8"/></svg>
        info@stridecare.example
      </span>
      <span class="contact-item">
        <svg width="14" height="14" viewBox="0 0 16 16"><circle cx="8" cy="8" r="6.5" fill="none" stroke="#fff" stroke-width="1.5"/><ellipse cx="8" cy="8" rx="3" ry="6.5" fill="none" stroke="#fff" stroke-width="1.2"/><line x1="1.5" y1="8" x2="14.5" y2="8" stroke="#fff" stroke-width="1.2"/></svg>
        www.stridecare.example
      </span>
    </footer>
  </section>

  <section class="card card-front">
    <svg class="accent" width="270" height="161" viewBox="0 0 270 161">
      <polygon points="0,0 82,0 0,48" fill="var(--orange)"/>
      <polygon points="38,31 82,4 84,8 40,35" fill="var(--charcoal)"/>
      <polygon points="270,113 270,161 188,161" fill="var(--orange)"/>
      <polygon points="186,157 230,130 232,134 188,161" fill="var(--charcoal)"/>
    </svg>
    <div class="brand-name"><span class="brand-dot"></span>StrideCare</div>
  </section>

  <section class="card card-back">
    <svg class="accent" width="270" height="161" viewBox="0 0 270 161">
      <polygon points="183,0 270,0 270,161 263,161" fill="var(--orange)"/>
      <polygon points="214,73 220,68 266,161 258,161" fill="var(--charcoal)"/>
    </svg>
    <div class="brand-name"><span class="brand-dot"></span>StrideCare</div>
    <div class="holder">
      <p class="holder-name">John Doe</p>
      <p class="holder-role">Director</p>
    </div>
    <ul class="card-contacts">
      <li>000.111.1234 <span class="tag"><i></i></span></li>
      <li>info@stridecare.example <span class="tag"><i></i></span></li>
      <li>www.stridecare.example <span class="tag"><i></i></span></li>
    </ul>
  </section>

</main>
</body>
</html>
```